Tolvane - online store for farm produce

Online store selling fresh produce (vegetables, fruits, dairy products, meat, ...) from various farmers. Every farm has its own shopping window - order page - just like a really simple web store.

Please check the attached design brief and mock-ups for further details.

Target Market(s)

People looking for fresh vegetables, fruit, meat, ... delivered from farms

Industry/Entity Type

Farming

Coding

Coded - Design and coding required

Number of Pages Required

5+ page

Font styles to use
Sans Serif

Requirements
Must have
• Custom design. Good UX/UI design, very functional.
Responsive using bootstrap 12 point grid system

```html
<!DOCTYPE html>
<html lang="en">
<head>
<meta charset="utf-8">
<title>Tolvane – Farm Produce Store</title>
<link href="https://fonts.googleapis.com/css2?family=Poppins:wght@400;500;600;700;800&display=swap" rel="stylesheet">
<style>
:root{
  --green:#7fb719;
  --green-dark:#6da010;
  --orange:#f0892a;
  --navy:#10283a;
  --text:#4a5560;
  --mint:#e6f6e6;
  --mint-strong:#b5e6b5;
  --footer-bg:#f3f6fa;
  --white:#ffffff;
}
*{box-sizing:border-box;margin:0;padding:0}
html,body{width:1200px;height:4135px;overflow:hidden}
body{position:relative;font-family:'Poppins',sans-serif;color:var(--text);background:var(--white)}
.abs{position:absolute}
.btn{position:absolute;display:flex;align-items:center;justify-content:center;border-radius:26px;color:var(--white);font-weight:600;font-size:13px;text-transform:uppercase;letter-spacing:.3px}
.btn-green{background:var(--green)}
.btn-orange{background:var(--orange)}
h2.title{position:absolute;font-size:44px;font-weight:700;color:var(--navy);line-height:1.05}
.rule{position:absolute;height:3px;width:58px;background:#dde1e4}
p.body{position:absolute;font-size:15px;line-height:24px;color:var(--text)}
.photo{position:absolute;border-radius:12px}

/* header */
.site-header{position:absolute;left:0;top:0;width:1200px;height:88px;background:var(--white)}
.logo{font-weight:800;font-size:24px;color:var(--navy);letter-spacing:.5px}
.nav a{position:absolute;top:33px;font-size:14px;font-weight:500;color:var(--navy);text-decoration:none}

/* hero */
.hero{left:0;top:88px;width:1200px;height:592px;background:linear-gradient(120deg,#7a5a3a 0%,#c7472b 30%,#3f7b2a 55%,#e2b52a 75%,#9fbf3a 100%)}
.hero-shade{left:0;top:88px;width:700px;height:592px;background:linear-gradient(90deg,rgba(20,20,20,.45),rgba(20,20,20,0))}
.hero-kicker{left:88px;top:275px;color:var(--white);font-weight:600;font-size:17px}
.hero-title{left:86px;top:298px;color:var(--white);font-weight:800;font-size:58px;line-height:60px}
.slide-tab{top:350px;width:30px;height:68px;background:rgba(255,255,255,.25);color:var(--white);font-size:14px;display:flex;align-items:center;justify-content:center}

/* lists */
ul.ticks{position:absolute;list-style:none}
ul.ticks li{position:relative;padding-left:20px;font-size:15px;line-height:31px;color:var(--text)}
ul.ticks li::before{content:"";position:absolute;left:0;top:11px;width:10px;height:10px;border-radius:50%;background:var(--mint-strong)}

/* form */
.farmer-form{left:88px;top:2332px;width:452px;height:300px;border-radius:10px;background:linear-gradient(135deg,var(--green) 0%,#86bd1f 60%,var(--green-dark) 100%)}
.field{position:absolute;left:47px;width:360px;height:46px;border-radius:23px;background:var(--white);font-size:13px;color:#555;padding-left:26px;display:flex;align-items:center}

/* footer */
.footer{left:0;top:3603px;width:1200px;height:532px;background:var(--footer-bg)}
.foot-h{position:absolute;font-size:18px;font-weight:600;color:var(--navy)}
.foot-links{position:absolute;list-style:none;font-size:14px;color:var(--text);line-height:27px}
.vline{position:absolute;width:1px;height:150px;background:#dfe3e8;top:3818px}
.social{position:absolute;top:3925px;width:30px;height:30px;border-radius:50%}
.contact-label{font-size:13px;font-weight:600;color:var(--navy)}
.contact-val{font-size:14px;color:var(--text);line-height:18px}
</style>
</head>
<body>

<!-- header -->
<header class="site-header">
  <div class="abs logo" style="left:88px;top:26px">TOLVANE</div>
  <nav class="nav">
    <a style="left:429px">HOME</a>
    <a style="left:523px">CURRENT OFFER</a>
    <a style="left:696px">SETTINGS</a>
  </nav>
  <div class="btn btn-green" style="left:946px;top:24px;width:94px;height:38px;font-size:13px">
    <svg width="12" height="12" viewBox="0 0 12 12" style="margin-right:4px"><circle cx="6" cy="3.5" r="3" fill="#fff"/><path d="M0 12c0-4 3-6 6-6s6 2 6 6z" fill="#fff"/></svg>LOGIN
  </div>
  <div class="abs" style="left:1052px;top:33px;font-size:14px;font-weight:600;color:var(--navy)">LOGOUT</div>
</header>

<!-- hero -->
<div class="abs hero" role="img" aria-label="Market stall piled with fresh tomatoes, peppers and greens"></div>
<div class="abs hero-shade"></div>
<div class="abs hero-kicker">EXTRA 50% OFF FOR ALL PRODUCT</div>
<div class="abs hero-title">Build Your Health<br>Eating Tolvane</div>
<div class="btn btn-orange" style="left:88px;top:439px;width:208px;height:46px">
  <svg width="12" height="13" viewBox="0 0 12 13" style="margin-right:6px"><path d="M0 0l12 6.5L0 13z" fill="#fff"/></svg>WATCH A VIDEO PLAY
</div>
<div class="abs slide-tab" style="left:0">‹</div>
<div class="abs slide-tab" style="left:1170px">›</div>

<!-- orange swoosh + green dot -->
<svg class="abs" style="left:0;top:600px" width="340" height="520" viewBox="0 0 340 520">
  <path d="M0 0 C40 90 90 130 180 150 C260 170 300 200 330 220 L0 520 Z" fill="var(--orange)"/>
</svg>
<div class="abs" style="left:205px;top:722px;width:50px;height:50px;border-radius:50%;background:var(--mint-strong);border:4px solid #fff"></div>

<!-- about -->
<div class="photo" style="left:138px;top:817px;width:442px;height:443px;background:linear-gradient(135deg,#e8e4df,#c3877f 50%,#b0a58c);box-shadow:0 20px 30px rgba(0,0,0,.15)" role="img" aria-label="Hands slicing a raw rack of meat on a cutting board with vegetables"></div>
<h2 class="title" style="left:658px;top:862px">What is this about</h2>
<div class="rule" style="left:633px;top:919px"></div>
<p class="body" style="left:658px;top:943px;width:455px">Lorem ipsum dolor sit amet, consectetur adipisicing elit, sed do eiusmod tempor incididunt ut labore et dolore magna aliqua. Ut enim ad minim veniam, quis nostrud exercitation ullamco laboris nisi ut aliquip ex ea commodo consequat. Duis aute irure dolor in reprehenderit in voluptate velit esse cillum dolore eu fugiat nulla pariatur.</p>
<p class="body" style="left:658px;top:1106px;width:455px">Excepteur sint runt mollit anim id est laborum. Sed ut atis unde omnis iste natus error sit volu</p>
<div class="btn btn-green" style="left:658px;top:1182px;width:165px;height:48px">PRODUCT SEARCH</div>

<!-- customer benefits -->
<div class="abs" style="left:1040px;top:1292px;width:230px;height:223px;border-radius:50%;background:var(--mint)"></div>
<h2 class="title" style="left:88px;top:1440px">Customer benefits</h2>
<div class="rule" style="left:62px;top:1496px"></div>
<ul class="ticks" style="left:88px;top:1517px">
  <li>Lorem ipsum dolor sit amet consectetur adipisicing elit,</li>
  <li>Sed do eiusmod tempor incididunt ut labore</li>
  <li>Ut enim ad minim veniam &nbsp;nostrud exercitation ullamco</li>
  <li>laboris nisi ut aliquip ex ea commodo consequat.</li>
  <li>Duis aute irure dolor in reprehenderit</li>
  <li>velit esse cillum dolore eu fugiat nulla pariatur. Excepteur</li>
  <li>Sint occaecat cupidatat non proident,</li>
  <li>Sunt in culpa qui deserunt mollit anim id est laborum</li>
</ul>
<div class="btn btn-green" style="left:88px;top:1787px;width:165px;height:48px">PRODUCT SEARCH</div>
<div class="photo" style="left:670px;top:1428px;width:435px;height:435px;background:linear-gradient(160deg,#6a7b3a,#c8a77a 45%,#b3402c 80%,#5b3a2a);border:3px solid #fff" role="img" aria-label="Shopper holding a paper bag full of fresh vegetables at a market"></div>

<!-- farmer benefits -->
<h2 class="title" style="left:0;width:1200px;text-align:center;top:1990px">Farmer benefits</h2>
<div class="rule" style="left:571px;top:2046px"></div>
<ul class="ticks" style="left:130px;top:2068px">
  <li>Lorem ipsum dolor sit amet consectetur adipisicing elit,</li>
  <li>Sed do eiusmod tempor incididunt ut labore</li>
  <li>Ut enim ad minim veniam &nbsp;nostrud exercitation ullamco</li>
  <li>laboris nisi ut aliquip ex ea commodo consequat.</li>
</ul>
<ul class="ticks" style="left:618px;top:2068px">
  <li>Duis aute irure dolor in reprehenderit</li>
  <li>velit esse cillum dolore eu fugiat nulla pariatur. Excepteur</li>
  <li>Sint occaecat cupidatat non proident,</li>
  <li>Sunt in culpa qui deserunt mollit anim id est laborum</li>
</ul>
<div class="abs" style="left:255px;top:2620px;font-size:190px;font-weight:800;color:#f2f3f5;letter-spacing:2px;line-height:1">Farmers</div>
<div class="photo" style="left:393px;top:2222px;width:717px;height:476px;background:linear-gradient(120deg,#9bb86a,#d9c08a 40%,#5d8a3a 70%,#c77a3a)" role="img" aria-label="Farmer in a straw hat carrying a crate of fresh carrots and vegetables"></div>
<div class="abs" style="left:298px;top:2298px;width:287px;height:290px;border:6px solid var(--green);border-radius:10px"></div>
<div class="abs farmer-form">
  <div class="field" style="top:32px">Company Name*</div>
  <div class="field" style="top:92px">Full Name*</div>
  <div class="field" style="top:152px">E-mail*</div>
  <div class="btn btn-orange" style="left:145px;top:223px;width:164px;height:46px">TELL ME MORE</div>
</div>

<!-- featured -->
<div class="abs" style="left:-80px;top:3280px;width:280px;height:280px;border-radius:50%;background:var(--mint)"></div>
<div class="photo" style="left:93px;top:2932px;width:484px;height:431px;background:linear-gradient(135deg,#6c8aa8,#3c4a52 50%,#9c9a8a);border:3px solid #fff" role="img" aria-label="Farmer with a tablet checking cows in a barn"></div>
<h2 class="title" style="left:658px;top:2940px">Featured farm or<br>product</h2>
<div class="rule" style="left:633px;top:3037px"></div>
<p class="body" style="left:658px;top:3060px;width:455px">Lorem ipsum dolor sit amet, consectetur adipisicing elit, sed do eiusmod tempor incididunt ut labore et dolore magna aliqua. Ut enim ad minim veniam, quis nostrud exercitation ullamco laboris nisi ut aliquip ex ea commodo consequat. Duis aute irure dolor in reprehenderit in voluptate velit esse cillum dolore eu fugiat nulla pariatur.</p>
<p class="body" style="left:658px;top:3223px;width:455px">Excepteur sint runt mollit anim id est laborum. Sed ut atis unde omnis iste natus error sit volu</p>
<div class="btn btn-green" style="left:658px;top:3302px;width:165px;height:48px">OUR FARM</div>

<!-- vegetable border -->
<div class="abs" style="left:0;top:3470px;width:1200px;height:133px;background:linear-gradient(90deg,#c9432b,#e59b2a 18%,#4f8a2a 35%,#8a3a6a 45%,#d6c23a 60%,#6fae2a 75%,#c9432b 88%,#4f8a2a)" role="img" aria-label="Row of fresh vegetables: tomatoes, carrots, cabbage, peppers and romanesco"></div>

<!-- footer -->
<footer class="abs footer"></footer>
<h2 class="title" style="left:0;width:1200px;text-align:center;top:3660px;font-size:40px">Newsletter</h2>
<div class="abs" style="left:276px;top:3715px;width:644px;height:47px;border-radius:24px;background:#fff;box-shadow:0 4px 12px rgba(0,0,0,.05)"></div>
<svg class="abs" style="left:301px;top:3732px" width="18" height="13" viewBox="0 0 18 13"><rect x="0.5" y="0.5" width="17" height="12" rx="1.5" fill="#c3c9d0"/><path d="M1 1l8 6 8-6" stroke="#fff" stroke-width="1.4" fill="none"/></svg>
<div class="abs" style="left:328px;top:3728px;font-size:15px;color:#777">Enter your email address</div>
<div class="btn btn-green" style="left:756px;top:3717px;width:162px;height:43px;font-size:14px">SUBSCRIBE</div>

<div class="abs logo" style="left:88px;top:3876px;font-size:34px">TOLVANE</div>
<div class="social" style="left:118px;background:#3b5ba0"></div>
<div class="social" style="left:159px;background:#28a9e6"></div>
<div class="social" style="left:200px;background:#e03b2e"></div>
<div class="social" style="left:241px;background:#a23aa3"></div>

<div class="vline" style="left:345px"></div>
<div class="vline" style="left:561px"></div>
<div class="vline" style="left:828px"></div>

<div class="foot-h" style="left:397px;top:3806px">Quick Links</div>
<ul class="foot-links" style="left:397px;top:3851px">
  <li>Home</li><li>Current Offer</li><li>Settings</li><li>Login/Logout</li>
</ul>
<div class="foot-h" style="left:627px;top:3808px">Information</div>
<ul class="foot-links" style="left:627px;top:3851px">
  <li>Terms of use</li><li>Terms and Conditions</li><li>Privacy Policy</li><li>About Us</li><li>FAQ</li>
</ul>
<div class="foot-h" style="left:883px;top:3808px">Contact Info</div>
<svg class="abs" style="left:883px;top:3856px" width="12" height="12" viewBox="0 0 12 12"><path d="M2 0h3l1 3-2 1a7 7 0 0 0 4 4l1-2 3 1v3a1 1 0 0 1-1 1A11 11 0 0 1 1 1a1 1 0 0 1 1-1z" fill="var(--orange)"/></svg>
<div class="abs" style="left:905px;top:3851px"><div class="contact-label">Phone</div><div class="contact-val">+08 555 014 2290</div></div>
<svg class="abs" style="left:883px;top:3910px" width="13" height="10" viewBox="0 0 13 10"><rect width="13" height="10" rx="1" fill="var(--orange)"/><path d="M1 1l5.5 4L12 1" stroke="#fff" fill="none"/></svg>
<div class="abs" style="left:905px;top:3904px"><div class="contact-label">Email</div><div class="contact-val">hello@tolvane-mail.test</div></div>
<svg class="abs" style="left:883px;top:3962px" width="10" height="14" viewBox="0 0 10 14"><path d="M5 0a5 5 0 0 1 5 5c0 4-5 9-5 9S0 9 0 5a5 5 0 0 1 5-5z" fill="var(--orange)"/><circle cx="5" cy="5" r="2" fill="#fff"/></svg>
<div class="abs" style="left:905px;top:3958px"><div class="contact-label">Location</div><div class="contact-val">Some address line goes here<br>city name country</div></div>

<div class="abs" style="left:88px;top:4073px;width:1024px;height:1px;background:#dfe3e8"></div>
<div class="abs" style="left:0;width:1200px;text-align:center;top:4092px;font-size:13px;color:var(--navy)">© 2020 Copyright - Verdale Studio All Rights Reserved</div>
<div class="abs" style="left:1129px;top:4049px;width:40px;height:40px;border-radius:50%;background:var(--orange);display:flex;align-items:center;justify-content:center">
  <svg width="10" height="6" viewBox="0 0 10 6"><path d="M1 5l4-4 4 4" stroke="#fff" stroke-width="1.6" fill="none"/></svg>
</div>

</body>
</html>
```